Calder Ridge Minerals

Looking for a cool, glossy business card...white with our logo on one side and then the a smaller version of the logo on the other side (top left hand corner) and then the name and position of the person next to it, and then the office address and email address on the bottom left hand corner and the phone numbers & email address on the bottom right hand corner. I have the logo already...can pass it on when you're ready.

```html
<!DOCTYPE html>
<html lang="en">
<head>
<meta charset="utf-8">
<title>Calder Ridge Minerals – Business Card</title>
<link rel="stylesheet" href="https://fonts.googleapis.com/css2?family=Cinzel:wght@400&family=Arimo:wght@400;700&display=swap">
<style>
  :root {
    --stage: #1c1c1e;
    --brand-red: #b3000f;
    --brand-purple: #5a1a9a;
    --brand-blue: #0d0dc0;
    --deep-blue: #0a0aa8;
    --paper: #ffffff;
    --ink: #1a1a1a;
  }
  * { box-sizing: border-box; margin: 0; padding: 0; }
  html, body { width: 1200px; height: 1015px; overflow: hidden; }
  body {
    background: var(--stage);
    display: flex;
    flex-direction: column;
    align-items: center;
    justify-content: center;
    gap: 56px;
    font-family: "Arimo", Arial, sans-serif;
  }
  .card {
    position: relative;
    width: 760px;
    height: 434px;
    overflow: hidden;
    border-radius: 4px;
    box-shadow: 0 18px 40px rgba(0,0,0,.55);
  }

  /* Logo side */
  .card--logo {
    background:
      radial-gradient(ellipse at 30% 60%, rgba(120,40,200,.35), transparent 60%),
      linear-gradient(160deg, var(--brand-red) 0%, #8a0d52 30%, var(--brand-purple) 55%, var(--brand-blue) 85%);
  }
  .logo-art {
    position: absolute;
    left: 230px;
    top: 78px;
    width: 300px;
    height: 170px;
    border-radius: 40% 55% 30% 45%;
    background: linear-gradient(120deg, rgba(255,255,255,.85), rgba(255,255,255,.6));
  }
  .wordmark {
    font-family: "Cinzel", Georgia, serif;
    font-weight: 400;
    letter-spacing: .08em;
    white-space: nowrap;
  }
  .card--logo .wordmark {
    position: absolute;
    left: 0; right: 0;
    top: 280px;
    text-align: center;
    color: var(--paper);
    font-size: 36px;
  }

  /* Contact side */
  .card--contact { background: var(--paper); }
  .wave { position: absolute; inset: 0; }
  .contact-logo-art {
    position: absolute;
    left: 52px;
    top: 80px;
    width: 250px;
    height: 110px;
    border-radius: 30% 50% 25% 40%;
    background: linear-gradient(100deg, var(--brand-blue) 0%, #5a63e0 30%, #e6e6e6 50%, #d01020 72%, var(--brand-red) 100%);
  }
  .card--contact .wordmark {
    position: absolute;
    left: 40px;
    top: 204px;
    color: var(--ink);
    font-size: 23px;
  }
  .person {
    position: absolute;
    right: 44px;
    top: 40px;
    text-align: right;
  }
  .person__name {
    color: var(--brand-blue);
    font-weight: 700;
    font-size: 28px;
    letter-spacing: .01em;
  }
  .person__role {
    color: var(--ink);
    font-size: 19px;
    margin-top: 2px;
  }
  .contact-list {
    position: absolute;
    right: 36px;
    top: 200px;
    list-style: none;
    color: var(--paper);
    font-size: 19px;
    line-height: 1.3;
    text-align: right;
  }
  .contact-list li {
    display: flex;
    justify-content: flex-end;
    align-items: center;
    gap: 10px;
  }
  .contact-list .address { margin-top: 6px; align-items: flex-start; }
  .icon { width: 18px; height: 18px; flex: none; }
</style>
</head>
<body>

  <section class="card card--logo" aria-label="Business card, logo side">
    <div class="logo-art" role="img" aria-label="White brush-stroke emblem of the company logo"></div>
    <p class="wordmark">Calder Ridge Minerals</p>
  </section>

  <section class="card card--contact" aria-label="Business card, contact side">
    <svg class="wave" viewBox="0 0 760 434" preserveAspectRatio="none" aria-hidden="true">
      <path d="M0,334 C220,334 320,304 420,228 C520,152 610,142 760,132 L760,138 C615,148 525,160 428,235 C330,311 225,345 0,345 Z" fill="var(--brand-red)"/>
      <path d="M0,358 C230,358 335,324 440,243 C540,165 630,152 760,146 L760,434 L0,434 Z" fill="var(--deep-blue)"/>
      <path d="M0,366 C235,366 340,332 446,251 C546,173 636,160 760,154" fill="none" stroke="var(--paper)" stroke-width="3"/>
    </svg>

    <div class="contact-logo-art" role="img" aria-label="Painted brush-stroke flag emblem of the company logo"></div>
    <p class="wordmark">Calder Ridge Minerals</p>

    <div class="person">
      <p class="person__name">MARCUS HALE</p>
      <p class="person__role">Managing Director</p>
    </div>

    <ul class="contact-list">
      <li>044-987 650 312
        <svg class="icon" viewBox="0 0 24 24"><path fill="#fff" d="M6.6 10.8a15 15 0 0 0 6.6 6.6l2.2-2.2a1 1 0 0 1 1-.25 11.4 11.4 0 0 0 3.6.57 1 1 0 0 1 1 1V20a1 1 0 0 1-1 1A17 17 0 0 1 3 4a1 1 0 0 1 1-1h3.5a1 1 0 0 1 1 1c0 1.25.2 2.45.57 3.57a1 1 0 0 1-.25 1z"/></svg>
      </li>
      <li>hello@calderridge.com
        <svg class="icon" viewBox="0 0 24 24"><path fill="#fff" d="M3 5h18v14H3z"/><path fill="none" stroke="var(--deep-blue)" stroke-width="1.6" d="M3 5l9 7 9-7"/></svg>
      </li>
      <li>www.calderridge.com
        <svg class="icon" viewBox="0 0 24 24" fill="none" stroke="#fff" stroke-width="1.8"><circle cx="12" cy="12" r="9"/><path d="M3 12h18M12 3c3 3 3 15 0 18M12 3c-3 3-3 15 0 18"/></svg>
      </li>
      <li class="address">88, Quarry Lane Suite 4<br>Redstone, 70318
        <svg class="icon" viewBox="0 0 24 24"><path fill="#fff" d="M12 2a7 7 0 0 0-7 7c0 5 7 13 7 13s7-8 7-13a7 7 0 0 0-7-7zm0 9.5A2.5 2.5 0 1 1 12 6.5a2.5 2.5 0 0 1 0 5z"/></svg>
      </li>
    </ul>
  </section>

</body>
</html>
```